Business Card Design Project

We need a business card design for an existing company in Dallas/Fort Worth that is expanding services and re-branding. We are changing the name from Brightmoor Commercial Cleaning to Keystride Facility Services. We are expanding from only commercial cleaning to include complete commercial landscape and facility maintenance services, too.

As stated, we offer a package of services that includes landscape, janitorial and facility services, which is largely unique in the industry.

We would like a design that communicates trust/partnership with a professional, corporate image, but not necessarily using the standard white business card. We would like a design that perhaps uses darker blues or perhaps a gray background, but we are open to other ideas. We might also be interested in a double-sided design - maybe with our logo on the back, printed on a gray background?

We will probably stick with the attached logo, but if you've got another inspired idea....

Target Market(s)

Property managers, commercial real estate professionals, corporate executives

Industry/Entity Type

Landscape

Requirements
Should not have
• Not interested in old style fonts.

```html
<!DOCTYPE html>
<html lang="en">
<head>
<meta charset="utf-8">
<title>Keystride Facility Services – Business Card</title>
<link rel="stylesheet" href="https://fonts.googleapis.com/css2?family=Open+Sans:wght@400;600;700;800&display=swap">
<style>
  :root {
    --backdrop-light: #f7f9f3;
    --backdrop-tint: #e3efd2;
    --card-black: #1c1c1c;
    --card-gray: #3b3b3b;
    --accent-yellow: #f2d21b;
    --text-white: #f2f2f2;
    --text-muted: #cfcfcf;
    --name-gray: #bdbdbd;
  }
  * { box-sizing: border-box; margin: 0; padding: 0; }
  html, body { width: 1200px; height: 646px; overflow: hidden; }
  body {
    position: relative;
    background: linear-gradient(120deg, var(--backdrop-light) 0%, var(--backdrop-light) 45%, var(--backdrop-tint) 100%);
    font-family: "Open Sans", Arial, sans-serif;
  }
  .card {
    position: absolute;
    top: 168px;
    width: 540px;
    height: 310px;
    background: var(--card-gray);
    box-shadow: 0 10px 28px rgba(0,0,0,.28);
    overflow: hidden;
  }
  .card--front { left: 45px; }
  .card--back { left: 615px; }
  .band {
    position: absolute;
    left: 0;
    width: 100%;
    background: var(--card-black);
  }
  .band--top { top: 0; height: 34px; border-bottom: 2px solid var(--accent-yellow); }
  .band--bottom {
    bottom: 0; height: 62px;
    border-top: 2px solid var(--accent-yellow);
    display: flex; align-items: center; justify-content: center;
  }
  .website {
    font-weight: 700;
    font-size: 19px;
    letter-spacing: 1.6px;
    color: var(--accent-yellow);
  }
  /* Front side */
  .front-brand {
    position: absolute;
    left: 56px; top: 78px;
    display: flex; align-items: center; gap: 20px;
  }
  .brand-square {
    width: 92px; height: 92px;
    border: 4px solid var(--text-white);
    background: var(--card-black);
    flex: none;
  }
  .brand-name {
    font-weight: 800;
    color: var(--accent-yellow);
    text-transform: uppercase;
    line-height: 1.05;
  }
  .front-brand .brand-name { font-size: 36px; letter-spacing: 2px; }
  .front-brand .brand-name small { display: block; font-size: 22px; letter-spacing: 2.4px; }
  .tagline { color: var(--text-muted); font-size: 13px; margin-top: 6px; letter-spacing: .2px; }
  /* Back side */
  .back-brand {
    position: absolute;
    left: 30px; top: 56px;
    width: 230px;
    text-align: center;
  }
  .back-brand .brand-square { width: 74px; height: 74px; margin: 0 auto 12px; }
  .back-brand .brand-name { font-size: 24px; letter-spacing: 1.5px; }
  .back-brand .brand-name small { display: block; font-size: 16px; letter-spacing: 1.6px; }
  .back-brand .tagline { font-size: 13px; line-height: 1.35; margin-top: 8px; }
  .contact {
    position: absolute;
    left: 285px; top: 58px;
  }
  .contact-name { font-size: 22px; font-weight: 700; color: var(--name-gray); line-height: 1.1; }
  .contact-role { font-size: 13px; font-weight: 600; color: var(--accent-yellow); margin: 2px 0 10px; }
  .contact-list { list-style: none; }
  .contact-list li {
    display: flex; align-items: center; gap: 7px;
    font-size: 12.5px; color: var(--text-white); margin-bottom: 4px;
  }
  .contact-key {
    width: 17px; height: 19px;
    background: var(--accent-yellow);
    color: var(--card-black);
    font-weight: 700; font-size: 12px;
    display: flex; align-items: center; justify-content: center;
    flex: none;
  }
</style>
</head>
<body>

<section class="card card--front" aria-label="Business card front">
  <div class="band band--top"></div>
  <div class="front-brand">
    <div class="brand-square"></div>
    <div>
      <div class="brand-name">Keystride<small>Facility Services</small></div>
      <p class="tagline">One Source For Landscape, Janitorial and Facility Maintenance</p>
    </div>
  </div>
  <div class="band band--bottom"><span class="website">www.keystridefacilityservices.com</span></div>
</section>

<section class="card card--back" aria-label="Business card back">
  <div class="band band--top"></div>
  <div class="back-brand">
    <div class="brand-square"></div>
    <div class="brand-name">Keystride<small>Facility Services</small></div>
    <p class="tagline">One Source For Landscape,<br>Janitorial and Facility Maintenance</p>
  </div>
  <div class="contact">
    <p class="contact-name">Daniel Reyes</p>
    <p class="contact-role">Marketing</p>
    <ul class="contact-list">
      <li><span class="contact-key">A</span>48 Elm Row Harbor Point 52718</li>
      <li><span class="contact-key">M</span>06 0517 2290</li>
      <li><span class="contact-key">P</span>(555) 014 3387</li>
      <li><span class="contact-key">E</span>dreyes@kfs.com</li>
    </ul>
  </div>
  <div class="band band--bottom"><span class="website">www.keystridefacilityservices.com</span></div>
</section>

</body>
</html>
```